" Sou uma médica cirurgiã plástica que atendendo numa clínica (que não é própria), fazendo parte de uma equipe de cirurgiões plásticos mais experientes que atende pacientes classe A em São Paulo. Faço todos os tipos de cirurgia plástica, mas tenho uma maior foco nas cirurgias de face (bleroplastia, ritidoplastia), mamoplastia e transplante capilar, além de procedimentos (laser, preenchedores/harmonização facial, dravix). "

```html
<!DOCTYPE html>
<html lang="pt-BR">
<head>
<meta charset="UTF-8">
<title>Papel timbrado — Dra. Helena Vasconcelos</title>
<link href="https://fonts.googleapis.com/css2?family=Cormorant+Garamond:wght@500&family=Montserrat:wght@400;500&display=swap" rel="stylesheet">
<style>
  :root {
    --backdrop: #ecebea;
    --paper: #ffffff;
    --plum: #7a2a5c;
    --rose: #c58aa7;
    --blush: #f0d3de;
    --ink: #5a4a55;
  }
  * { margin: 0; padding: 0; box-sizing: border-box; }
  html, body { width: 1200px; height: 1200px; overflow: hidden; }
  body {
    background: var(--backdrop);
    font-family: "Montserrat", sans-serif;
    position: relative;
  }
  .letterhead {
    position: absolute;
    left: 270px; top: 120px;
    width: 660px; height: 960px;
    background: var(--paper);
    box-shadow: 0 6px 18px rgba(0,0,0,0.12);
  }
  .header-bar { position: absolute; top: 127px; height: 6px; }
  .header-bar--left { left: 7px; width: 281px; background: var(--plum); }
  .header-bar--right { left: 373px; width: 283px; background: var(--rose); }
  .brand-mark {
    position: absolute; left: 314px; top: 98px;
    width: 32px; height: 32px;
    border: 3px solid var(--rose);
    background: var(--paper);
  }
  .brand-name {
    position: absolute; left: 0; width: 660px; top: 146px;
    text-align: center;
    font-family: "Cormorant Garamond", serif;
    font-weight: 500; font-size: 24px;
    letter-spacing: 1px;
    color: var(--plum);
    text-transform: uppercase;
  }
  .brand-role {
    position: absolute; left: 0; width: 660px; top: 178px;
    text-align: center;
    font-size: 9px; font-weight: 500;
    letter-spacing: 2px;
    color: var(--plum);
    text-transform: uppercase;
  }
  .corner-frame {
    position: absolute; left: 7px; top: 571px;
    width: 388px; height: 323px;
    border: 5px solid var(--blush);
    border-left: none;
  }
  .footer-rule {
    position: absolute; left: 7px; top: 837px;
    width: 388px; height: 5px;
    background: var(--rose);
  }
  .contact {
    position: absolute; left: 410px; top: 782px;
    height: 112px;
    border-left: 3px solid var(--plum);
    padding-left: 14px; padding-top: 26px;
    font-size: 11px; color: var(--ink);
  }
  .contact__row { display: flex; align-items: flex-start; gap: 8px; line-height: 15px; }
  .contact__row svg { width: 10px; height: 10px; margin-top: 2px; flex: none; }
  .contact__row--address { margin-top: 10px; }
</style>
</head>
<body>
  <main class="letterhead">
    <div class="header-bar header-bar--left"></div>
    <div class="header-bar header-bar--right"></div>
    <div class="brand-mark"></div>
    <h1 class="brand-name">Dra. Helena Vasconcelos</h1>
    <p class="brand-role">Cirurgiã Plástica</p>

    <div class="corner-frame"></div>
    <div class="footer-rule"></div>

    <address class="contact" style="font-style:normal">
      <div class="contact__row">
        <svg viewBox="0 0 10 10"><path d="M2 0.5 L4 2.5 L3 4 Q4.5 6 6 7 L7.5 6 L9.5 8 L8 9.5 Q3.5 9 0.5 2 Z" fill="var(--ink)"/></svg>
        <span>(11) 5540-2187</span>
      </div>
      <div class="contact__row">
        <svg viewBox="0 0 10 10"><circle cx="5" cy="5" r="4" fill="none" stroke="var(--ink)" stroke-width="1.2"/><path d="M3.5 3 L4.3 4.2 Q5 5.6 6.2 6.3 L7 6.8" fill="none" stroke="var(--ink)" stroke-width="1"/></svg>
        <span>(11) 98431-726</span>
      </div>
      <div class="contact__row contact__row--address">
        <svg viewBox="0 0 10 10"><path d="M5 0.5 A3.3 3.3 0 0 1 8.3 3.8 Q8.3 6 5 9.5 Q1.7 6 1.7 3.8 A3.3 3.3 0 0 1 5 0.5 Z" fill="var(--ink)"/><circle cx="5" cy="3.8" r="1.2" fill="#fff"/></svg>
        <span>Alameda das Orquídeas nº 82<br>Jardins, São Paulo</span>
      </div>
    </address>
  </main>
</body>
</html>
```